Business Card Design Project

Hi!
Looking for a business card design for my acupuncture/remedial massage business using a logo I've just had designed through this site!
I'd like the following details included:
Logo (obviously)
My name - Miranda Pellowtane
Clinic details -Complementary and Traditional Chinese Medicine Haven
42 Brindlewood Road
Ashbury Vale 3162
03 9471 6820
Website - www.pellowtanewell.com.au
I have the logo design in two different colour combinations, one predominantly green, and the other in reverse colours. I was thinking that the green logo would take up one whole side of the business card, then we could include the reverse logo on the more detailed side. I'd like to see how that looks.
I also had the idea that the heart in the logo could be printed in metallic red (depending on cost). Not sure if that comes into play now or at the printers.
Thanks!

```html
<!DOCTYPE html>
<html lang="en">
<head>
<meta charset="utf-8">
<title>Pellow Well – Business Card</title>
<link href="https://fonts.googleapis.com/css2?family=Ubuntu:wght@400;500;700&family=Roboto+Condensed:wght@400&display=swap" rel="stylesheet">
<style>
  :root {
    --jade: #1bb585;
    --jade-soft: #9fdcc7;
    --paper: #ffffff;
    --ink: #2f3a36;
    --edge: #e3e6e5;
  }
  * { margin: 0; padding: 0; box-sizing: border-box; }
  html, body {
    width: 1200px;
    height: 416px;
    overflow: hidden;
    background: var(--paper);
    font-family: "Ubuntu", Arial, sans-serif;
  }
  .sheet { position: relative; width: 1200px; height: 416px; }

  .card { position: absolute; top: 0; height: 330px; }

  .card--front {
    left: 0;
    width: 587px;
    background: var(--jade);
    display: flex;
    align-items: center;
    justify-content: center;
  }

  .card--back {
    left: 612px;
    width: 588px;
    background: var(--paper);
    border-left: 1px solid var(--edge);
  }
  .card__band {
    position: absolute;
    left: 0; right: 0;
    height: 12px;
    background: var(--jade);
  }
  .card__band--top { top: 0; }
  .card__band--bottom { bottom: 0; }

  .brand-name {
    font-family: "Ubuntu", Arial, sans-serif;
    font-weight: 700;
    font-size: 54px;
    line-height: 1;
    letter-spacing: -0.5px;
    text-align: center;
    white-space: nowrap;
  }
  .card--front .brand-name { color: var(--paper); }
  .card--back .brand-name {
    position: absolute;
    left: 0;
    width: 234px;
    top: 142px;
    font-size: 36px;
    color: var(--jade);
  }

  .divider {
    position: absolute;
    left: 253px;
    top: 38px;
    width: 1px;
    height: 254px;
    background: var(--jade-soft);
  }

  .clinic-title {
    position: absolute;
    right: 41px;
    top: 24px;
    text-align: right;
    color: var(--jade);
    font-weight: 700;
    font-size: 23.5px;
    line-height: 31px;
    white-space: nowrap;
  }

  .person-name {
    position: absolute;
    right: 41px;
    top: 183px;
    color: var(--jade);
    font-weight: 700;
    font-size: 19.5px;
    line-height: 26px;
    white-space: nowrap;
  }

  .contact {
    position: absolute;
    right: 41px;
    top: 214px;
    list-style: none;
    color: var(--ink);
    font-family: "Roboto Condensed", "Arial Narrow", sans-serif;
    font-size: 16px;
    line-height: 23px;
    white-space: nowrap;
  }
  .contact__row {
    display: flex;
    justify-content: flex-end;
    align-items: center;
    gap: 12px;
  }
  .contact__icon {
    width: 14px;
    height: 14px;
    flex: none;
    color: var(--jade);
  }
  .contact__icon--blank { visibility: hidden; }
</style>
</head>
<body>
<main class="sheet">

  <section class="card card--front" aria-label="Card front">
    <p class="brand-name">Pellow Well</p>
  </section>

  <section class="card card--back" aria-label="Card back">
    <div class="card__band card__band--top"></div>

    <p class="brand-name">Pellow Well</p>

    <div class="divider"></div>

    <h1 class="clinic-title">Complementary &amp;<br>Traditional Chinese<br>Medicine Haven</h1>

    <h2 class="person-name">Miranda Pellowtane</h2>

    <ul class="contact">
      <li class="contact__row">
        <span>42 Brindlewood Road</span>
        <svg class="contact__icon" viewBox="0 0 14 14" aria-hidden="true">
          <path d="M7 0.5a4.6 4.6 0 0 0-4.6 4.6C2.4 8.6 7 13.5 7 13.5s4.6-4.9 4.6-8.4A4.6 4.6 0 0 0 7 0.5zm0 6.4a1.8 1.8 0 1 1 0-3.6 1.8 1.8 0 0 1 0 3.6z" fill="currentColor"/>
        </svg>
      </li>
      <li class="contact__row">
        <span>Ashbury Vale 3162</span>
        <svg class="contact__icon contact__icon--blank" viewBox="0 0 14 14" aria-hidden="true"></svg>
      </li>
      <li class="contact__row">
        <span>03 9471 6820</span>
        <svg class="contact__icon" viewBox="0 0 14 14" aria-hidden="true">
          <path d="M3.2 1.2l2 2.4-1.1 1.5c.8 1.8 2.1 3.1 3.9 3.9l1.5-1.1 2.4 2-1.3 2.1C5.9 11.7 2.3 8.1 1.1 3.4z" fill="currentColor"/>
        </svg>
      </li>
      <li class="contact__row">
        <span>www.pellowtanewell.com.au</span>
        <svg class="contact__icon" viewBox="0 0 14 14" aria-hidden="true">
          <g fill="none" stroke="currentColor" stroke-width="1.3">
            <circle cx="7" cy="7" r="5.8"/>
            <ellipse cx="7" cy="7" rx="2.5" ry="5.8"/>
            <path d="M1.2 7h11.6M2 4h10M2 10h10"/>
          </g>
        </svg>
      </li>
    </ul>

    <div class="card__band card__band--bottom"></div>
  </section>

</main>
</body>
</html>
```